SUMMIT GATHERING 2021. August 20th -22nd.

The Hosts of the conference: Grace Tabernacle-Pastors Ron n Della ( Picture with two persons)

Guest Minister: Bishop Lucinda Okotieno. (Cedar Ridge Awakening)

Venue:
Sealand Gateway Lodgeview. 4817 North 239th Avenue Seattle, WA 98174.

Conference times.
Friday August 20th 6pm-8:30pm
Saturday August 21st. 6pm-8:30pm

Sunday August 22nd 10am-1pm
“ CHURCH RENEWAL GATHERING”

5pm-7:30pm
TWOFOLD SURGE GATHERING.

Target Market(s)

18-55

Industry/Entity Type

Religious/ Entertainment.

Requirements
Must have
• A highlight of the Relaunch service on Sunday August 22nd 5pm-7:30pm.
Nice to have
• Excellent ideas….

```html
<!DOCTYPE html>
<html lang="en">
<head>
<meta charset="utf-8">
<title>Summit Gathering 2021</title>
<link href="https://fonts.googleapis.com/css2?family=Anton&family=Oswald:wght@400;500;600;700&family=Montserrat:wght@600;700&display=swap" rel="stylesheet">
<style>
  :root {
    --ink: #0b0b10;
    --red: #e3000f;
    --red-deep: #8f0a0a;
    --gold-hi: #f3e7b8;
    --gold: #c9a85a;
    --gold-lo: #8a6a2a;
    --white: #ffffff;
    --text-dark: #1a1a1a;
  }
  * { margin: 0; padding: 0; box-sizing: border-box; }
  html, body { width: 720px; height: 1200px; overflow: hidden; background: var(--ink); }
  .poster {
    position: relative; width: 720px; height: 1200px; overflow: hidden;
    background:
      radial-gradient(ellipse 420px 260px at 640px 40px, rgba(200,40,20,.85), transparent 70%),
      radial-gradient(ellipse 500px 380px at 700px 300px, rgba(140,10,20,.7), transparent 75%),
      linear-gradient(180deg, #1a0a10 0%, #0b0b12 40%, #0d0f1a 100%);
    font-family: "Montserrat", sans-serif; color: var(--white);
  }
  .red-band { position: absolute; left: 0; top: 580px; width: 720px; height: 300px; background: var(--red); }
  .gold-text {
    background: linear-gradient(180deg, var(--gold-hi) 0%, var(--gold) 45%, var(--gold-lo) 60%, var(--gold-hi) 100%);
    -webkit-background-clip: text; background-clip: text; color: transparent;
  }
  .title { position: absolute; left: 46px; top: 44px; font-family: "Anton", sans-serif; font-size: 80px; line-height: 1; letter-spacing: 1px; white-space: nowrap; }
  .year { position: absolute; left: 44px; top: 132px; font-family: "Anton", sans-serif; font-size: 168px; line-height: 1; letter-spacing: -2px; }
  .date-box {
    position: absolute; left: 46px; top: 306px; width: 354px; height: 70px; background: var(--red);
    border-radius: 0 8px 8px 0; font-family: "Oswald", sans-serif; font-weight: 700; font-size: 44px;
    display: flex; align-items: center; justify-content: center; letter-spacing: -.5px; white-space: nowrap;
  }
  .info-label { position: absolute; left: 46px; font-size: 16px; font-weight: 600; color: var(--red); text-transform: uppercase; white-space: nowrap; }
  .info-value { position: absolute; left: 46px; font-size: 16px; font-weight: 700; white-space: nowrap; }
  .gold-badge {
    position: absolute; left: 46px; height: 40px; padding: 0 14px;
    background: linear-gradient(180deg, var(--gold-hi), var(--gold) 55%, #e8d59a);
    color: var(--text-dark); font-weight: 700; font-size: 20px; display: flex; align-items: center;
    border-radius: 3px; white-space: nowrap;
  }
  .icon-line { position: absolute; left: 46px; display: flex; align-items: flex-start; gap: 12px; font-weight: 700; font-size: 16px; line-height: 27px; white-space: nowrap; }
  .icon-line svg { flex: none; margin-top: 4px; }
  .sunday-box {
    position: absolute; left: 46px; top: 825px; width: 350px; height: 92px; border-radius: 0 12px 12px 0;
    background: linear-gradient(180deg, #f6ecc6, var(--gold) 60%, #b8954c);
    font-family: "Oswald", sans-serif; text-align: center; padding-top: 10px; white-space: nowrap;
  }
  .sunday-box .when { font-size: 26px; font-weight: 400; color: var(--text-dark); line-height: 1.25; }
  .sunday-box .what { font-size: 22px; font-weight: 700; color: var(--red); line-height: 1.4; }
  .clock { position: absolute; left: 60px; top: 944px; }
  .evening { position: absolute; left: 138px; top: 940px; white-space: nowrap; }
  .evening .time { font-size: 28px; font-weight: 700; line-height: 1.1; }
  .evening .name { font-size: 17px; font-weight: 700; color: var(--red); line-height: 1.4; }
  .brand { position: absolute; left: 46px; top: 1040px; width: 92px; text-align: center; }
  .brand-mark { width: 78px; height: 78px; margin: 0 auto 8px; background: linear-gradient(160deg, var(--gold-hi), var(--gold-lo)); }
  .brand-name { font-size: 11px; font-weight: 700; color: var(--white); line-height: 1.2; }
  .highlight { position: absolute; left: 154px; top: 1052px; font-family: "Oswald", sans-serif; white-space: nowrap; }
  .highlight .lead { font-size: 40px; font-weight: 400; line-height: 1.2; letter-spacing: .5px; }
  .highlight .main { font-size: 35px; font-weight: 700; line-height: 1.3; letter-spacing: 0; }
  .portraits { position: absolute; left: 0; top: 0; width: 720px; height: 1200px; pointer-events: none; }
</style>
</head>
<body>
<main class="poster">
  <div class="red-band"></div>

  <svg class="portraits" viewBox="0 0 720 1200">
    <defs>
      <linearGradient id="ring" x1="0" y1="0" x2="1" y2="1">
        <stop offset="0" stop-color="#f3e7b8"/><stop offset=".5" stop-color="#b08a3e"/><stop offset="1" stop-color="#f0dfa4"/>
      </linearGradient>
      <linearGradient id="hostsTone" x1="0" y1="0" x2="1" y2="1">
        <stop offset="0" stop-color="#3a2a4a"/><stop offset=".5" stop-color="#6a3a6e"/><stop offset="1" stop-color="#2a1a20"/>
      </linearGradient>
      <linearGradient id="guestTone" x1="0" y1="0" x2="0" y2="1">
        <stop offset="0" stop-color="#e8ece8"/><stop offset=".55" stop-color="#6b4a3a"/><stop offset="1" stop-color="#4a4a4a"/>
      </linearGradient>
    </defs>
    <circle cx="560" cy="470" r="212" fill="none" stroke="url(#ring)" stroke-width="4"/>
    <circle cx="580" cy="475" r="195" fill="url(#hostsTone)" role="img" aria-label="Photo of the hosts, Pastors Ron and Della"/>
    <circle cx="570" cy="862" r="166" fill="none" stroke="url(#ring)" stroke-width="4"/>
    <circle cx="570" cy="862" r="155" fill="url(#guestTone)" role="img" aria-label="Photo of the guest minister, Bishop Lucinda Okotieno"/>
  </svg>

  <h1 class="title gold-text">SUMMIT GATHERING</h1>
  <div class="year gold-text">2021</div>
  <div class="date-box">August 20th -22nd</div>

  <div class="info-label" style="top:404px">Hosts of the conference:</div>
  <div class="info-value" style="top:428px">Grace Tabernacle- Pastors Ron n Della</div>
  <div class="info-label" style="top:480px">Guest Minister:</div>
  <div class="info-value" style="top:504px">Bishop Lucinda Okotieno</div>

  <div class="gold-badge" style="top:562px">VENUE:</div>
  <div class="icon-line" style="top:616px">
    <svg width="18" height="22" viewBox="0 0 18 22"><path d="M9 1a7 7 0 0 0-7 7c0 5 7 12 7 12s7-7 7-12a7 7 0 0 0-7-7z" fill="none" stroke="#7a0a0a" stroke-width="2"/><circle cx="9" cy="8" r="2.5" fill="#7a0a0a"/></svg>
    <span>Sealand Gateway Lodgeview. 4817<br>North 239th Avenue Seattle, WA 98174.</span>
  </div>

  <div class="gold-badge" style="top:691px">CONFERENCE TIMES</div>
  <div class="icon-line" style="top:742px">
    <svg width="18" height="16" viewBox="0 0 18 16"><rect x="1" y="2" width="16" height="13" fill="#3a0a0a"/><rect x="1" y="2" width="16" height="4" fill="#1a0505"/></svg>
    <span>Friday August 20th 6pm-8:30pm</span>
  </div>
  <div class="icon-line" style="top:776px">
    <svg width="18" height="16" viewBox="0 0 18 16"><rect x="1" y="2" width="16" height="13" fill="#3a0a0a"/><rect x="1" y="2" width="16" height="4" fill="#1a0505"/></svg>
    <span>Saturday August 21st. 6pm-8:30pm</span>
  </div>

  <div class="sunday-box">
    <div class="when">Sunday August 22nd 10am-1pm</div>
    <div class="what">“ CHURCH RENEWAL GATHERING”</div>
  </div>

  <svg class="clock" width="66" height="66" viewBox="0 0 66 66">
    <circle cx="33" cy="33" r="29" fill="none" stroke="#e3000f" stroke-width="6"/>
    <circle cx="33" cy="33" r="19" fill="none" stroke="#e3000f" stroke-width="3"/>
    <path d="M33 21v12l-8 6" fill="none" stroke="#e3000f" stroke-width="3"/>
  </svg>
  <div class="evening">
    <div class="time">5pm-7:30pm</div>
    <div class="name">TWOFOLD SURGE GATHERING.</div>
  </div>

  <div class="brand">
    <div class="brand-mark"></div>
    <div class="brand-name">GRACE TABERNACLE</div>
  </div>
  <div class="highlight">
    <div class="lead">RELAUNCH SERVICE ON</div>
    <div class="main gold-text">SUNDAY AUGUST 22ND 5PM-7:30PM</div>
  </div>
</main>
</body>
</html>
```